Business Card Design for Technology Company

New business card design needed for technology company director.
Ideally, the design will fit the style and nature of the industry. We are a supplier of quality products and services, and we hope the design will give customers and suppliers this impression.

Target Market(s)

3D Printing Industry

Industry/Entity Type

Technology Equipment

Contact Information for Business Card

Name: Marcus Lyle
Title: Director
Company address: Factory K4, 7B Morland Road, Springvale Victoria Australia 3150
Telephone: +61-3-8555 6413
Email: marcus.lyle@veranox.com.au
Website: www.veranox.com.au

Requirements
Must have
• All information in business card details
• Company logo
• '3D Printers and 3D Print Filaments' at proper place
Nice to have
• Style to fit the industry
• Colour to fit logo

```html
<!DOCTYPE html>
<html lang="en">
<head>
<meta charset="utf-8">
<title>Veranox – Business Card</title>
<link rel="stylesheet" href="https://fonts.googleapis.com/css2?family=Montserrat:wght@400;600;700&family=Roboto:wght@400&display=swap">
<style>
  :root {
    --stage: #dcdcdc;
    --blue-deep: #0a3f78;
    --blue-mid: #0a5fa3;
    --blue-light: #0e7dbf;
    --grey-light: #f2f3f4;
    --grey-mid: #c4c7ca;
    --grey-dark: #8a8e92;
    --white: #ffffff;
    --ink: #111111;
    --ink-soft: #444444;
    --accent: #1b7fc4;
  }
  * { margin: 0; padding: 0; box-sizing: border-box; }
  html, body {
    width: 1125px; height: 1200px; overflow: hidden;
    background: var(--stage);
  }
  .canvas { position: relative; width: 1125px; height: 1200px; }
  .card {
    position: absolute; left: 156px; width: 825px; height: 471px;
    overflow: hidden;
    box-shadow: 0 6px 18px rgba(0,0,0,.22);
  }
  .card--front {
    top: 106px;
    background: radial-gradient(ellipse at 30% 65%, var(--blue-light) 0%, var(--blue-mid) 45%, var(--blue-deep) 100%);
    color: var(--white);
    font-family: "Montserrat", sans-serif;
  }
  .card--back { top: 639px; background: var(--white); }

  .front-visual {
    position: absolute; inset: 0;
    clip-path: polygon(394px 0, 825px 0, 825px 471px, 773px 471px, 394px 252px);
    background: radial-gradient(ellipse at 68% 40%, var(--grey-light) 0%, var(--grey-mid) 55%, var(--grey-dark) 100%);
  }
  .front-visual__edge {
    position: absolute; inset: 0;
    clip-path: polygon(394px 0, 404px 0, 404px 246px, 790px 471px, 773px 471px, 394px 252px);
    background: var(--grey-dark);
  }

  .front-brand {
    position: absolute; left: 41px; top: 82px;
    font-weight: 700; font-size: 40px; letter-spacing: 6px;
    color: var(--white);
  }
  .holder { position: absolute; left: 41px; top: 176px; }
  .holder__name { font-weight: 700; font-size: 29px; line-height: 32px; letter-spacing: .5px; text-transform: uppercase; }
  .holder__title { font-weight: 700; font-size: 20px; line-height: 22px; text-transform: uppercase; }

  .address {
    position: absolute; left: 43px; top: 264px;
    font-size: 19px; line-height: 25px; font-weight: 400; font-style: normal;
  }
  .contacts { position: absolute; left: 43px; top: 354px; list-style: none; }
  .contacts li {
    display: flex; align-items: center; gap: 10px;
    font-size: 19px; line-height: 26px;
  }
  .contacts svg { width: 17px; height: 17px; fill: var(--white); flex: none; }

  .back-brand {
    position: absolute; left: 0; right: 0; top: 196px;
    display: flex; align-items: center; justify-content: center; gap: 28px;
  }
  .back-brand__mark { width: 78px; height: 78px; background: var(--accent); }
  .back-brand__name {
    font-family: "Montserrat", sans-serif; font-weight: 700;
    font-size: 54px; letter-spacing: 8px; color: var(--ink);
  }
  .tagline {
    position: absolute; left: 0; right: 0; top: 400px; text-align: center;
    font-family: "Roboto", sans-serif; font-size: 19px; color: var(--ink-soft);
  }
</style>
</head>
<body>
<main class="canvas">
  <section class="card card--front">
    <div class="front-visual" role="img" aria-label="Grey metallic frame with light rays, rendered in silver tones"></div>
    <div class="front-visual__edge"></div>

    <div class="front-brand">VERANOX</div>

    <div class="holder">
      <p class="holder__name">Marcus Lyle</p>
      <p class="holder__title">Director</p>
    </div>

    <address class="address">
      Factory K4, 7B Morland Road,<br>
      Springvale Victoria<br>
      Australia 3150
    </address>

    <ul class="contacts">
      <li>
        <svg viewBox="0 0 24 24" aria-hidden="true"><path d="M6.6 10.8a15.2 15.2 0 0 0 6.6 6.6l2.2-2.2a1 1 0 0 1 1-.25 11.4 11.4 0 0 0 3.6.57 1 1 0 0 1 1 1V20a1 1 0 0 1-1 1A17 17 0 0 1 3 4a1 1 0 0 1 1-1h3.5a1 1 0 0 1 1 1c0 1.25.2 2.45.57 3.57a1 1 0 0 1-.25 1z"/></svg>
        +61-3-8555 6413
      </li>
      <li>
        <svg viewBox="0 0 24 24" aria-hidden="true"><path d="M2 5h20v14H2z M2 5l10 8 10-8" fill="none" stroke="#fff" stroke-width="2"/><path d="M2 6l10 7 10-7v13H2z"/></svg>
        marcus.lyle@veranox.com.au
      </li>
      <li>
        <svg viewBox="0 0 24 24" aria-hidden="true"><path d="M12 2a10 10 0 1 0 0 20 10 10 0 0 0 0-20zm-1 17.9A8 8 0 0 1 4.1 11H7l2 2v2l2 2zm6.9-2.5A2 2 0 0 0 16 16h-1v-3a1 1 0 0 0-1-1H8v-2h2a1 1 0 0 0 1-1V7h2a2 2 0 0 0 2-2v-.4a8 8 0 0 1 2.9 12.8z"/></svg>
        www.veranox.com.au
      </li>
    </ul>
  </section>

  <section class="card card--back">
    <div class="back-brand">
      <span class="back-brand__mark" aria-hidden="true"></span>
      <span class="back-brand__name">VERANOX</span>
    </div>
    <p class="tagline">3D Printers and 3D Print Filaments</p>
  </section>
</main>
</body>
</html>
```